Corporate website design needed

We need a Contemporary Industrial/Tech/Logistics Website design to match our logistic client's business. Our client consults and build logistics solutions that they manage but they are not a typical 3PL (3rd party logistics company) which is primarily engaged in moving boxes.
PSD file only for now, home and default templates.
COMPANY CHARACTER
DESIGN LOOK AND FEEL
• The design should also be modern and visually well organized — employing a combination of visual devices and info graphics. Keep it light and not too heavy but strong/ professional. And unique.
• The design should go beyond the typical industrial pick and pack 3PL representing [Logistics Company] as a High Tech/IT logistics company.
Some examples although these are not right for this client because they have much more content and present themselves more as a 3pl.
http://www.tg-gateway.example/ (More right then wrong - Like this but simplified)
http://www.morvanfreight.example (Ugly)
http://www.pdwellstead.example (More right then wrong but different focus)
http://www.halverinco.example/ Too 3PL trucking… We want a bit ore high level approach
The difference, the design should be a fusion in core concepts that culminate in a design which implies the following attributes. Tech (Big data / analytics / software), Consultancy (Solutions, SME, Leader), 3PL Industry vertical solutions.
NOTE: The visualization of “tech” is not “1” and “0”, but more “software and analytics” Perhaps more like www.quantelyx.example.
• They need to be seen as a solutions provider in Logistics and as in Subject matter experts
TONE
The tone needs to exude professionalism, expertise, though leadership along with technical and executional excellence.
Experienced
Knowledgeable
Confident
Determined
Straightforward
WEBSITE OBJECTIVES
• Focus C-Suite executives and logistics managers’ attention on [Logistics Company]s commanding knowledge and expertise, and unique approach to supply chain solutions producing more RFP wins
• Create an easy to scan design which decreases the reliance on text through featured text, summaries, and smaller “chunked” size bits of information.
• Convey [Logistics Company] as high-tech 3PL solutions developer and services provider with a ‘high-touch’ consultative approach.
• Showcase [Logistics Company]’s value propositions. (See Slider Content)
• Showcase [Logistics Company]’s expertise in logistical analytics.
• Gain recognition as an industry leader in evolutionary new space (supply chain 2.0)
WEBSITE STRATEGY
• Reduce reliance on text (at least within initial entry points for each section)
• Typography: Watch text line lengths and readability, bolder fonts. NO SERIFS
• Generally, create a click-through format so that users who want more details can find it, and those who don’t can get a snapshot without clicking through.
• Increase visual content through info graphics and some dynamic content, photography
• Better utilize the space on each page (e.g., add visual interest, photography and iconography where appropriate to break up copy blocks and maintain readable line lengths).
COLOR SCHEME
• Create a more engaging color scheme (the logo will remain the same under all circumstances).
• Red / grayscale may work…. Not too dark or heavy. Not too much red. Ex. parvixa.example
• Also try blues and greys. They seem to like that. Open to suggestions but don’t get to crazy. Red is in their logo but too much may be a problem.
PHOTOGRAPHY
Yes. And I will upload some.
If you pick photography please be sure to note Which stock house used and the image number!
CONTENT
The content will be presented in a more hierarchical format — with lead-ins, paragraph and section headers and navigational cues to expand lengthier content allowing the visitor to more easily scan the website. No case studies, No Social media, News while on the home page should not be over emphasized. They don't post a lot so it gets dated quickly ...
I will be uploading a wire frame and other elements.
NOTE: I uploaded my EXAMPLE mock up which is close but not close enough.
I am not a great designer. So I am looking for an alternative that exceed my design ability! These examples show the basic layout but I really want some varied alternatives.
The colors are inconsistent and type not quite right. The grey bar at top is not right and should probably go away.
Please pull the basic elements in the example together into a great design.
If you have questions please contact me.
i will upload some photography tomorrow that may be of use.
Thanks!
Updates
Hi All,
We are still evaluating the submitted designs. Sorry for the delay.
Target Market(s)
This website is primarily a validation website. Few new customers will search and find them as such...
The site should be Focused on C-Suite executives and logistics managers’ attention on [Logistics Company]s commanding knowledge and expertise, and unique approach to supply chain solutions producing more RFP wins
Industry/Entity Type
Business
Requirements
Must have
- Slide show, Clearly explain who they are and what they do.
Create an easy to scan design which decreases the reliance on text through featured text, summaries, and smaller “chunked” size bits of information.
Convey [Logistics Company] as high-tech 3PL solutions developer and services
provider with a ‘high-touch’ consultative approach.
Should not have
- No Ads space
No Social media
Not too cluttered. Keep it clean.

```html
<!DOCTYPE html>
<html lang="en">
<head>
<meta charset="utf-8">
<title>Vantreal Logistics</title>
<link href="https://fonts.googleapis.com/css2?family=Open+Sans:wght@400;600;700&display=swap" rel="stylesheet">
<style>
:root{
  --blue:#1b86c6;
  --navy:#0f4a70;
  --red:#c8102e;
  --dark:#1c1c1c;
  --nav:#262626;
  --text:#555;
  --band:#ebebeb;
  --page:#f2f2f2;
  --white:#fff;
}
*{box-sizing:border-box;margin:0;padding:0}
html,body{width:777px;height:1200px;overflow:hidden}
body{background:var(--page);font-family:'Open Sans',Arial,sans-serif;color:var(--text);position:relative}
.page{position:absolute;left:78px;top:0;width:621px;height:1200px;background:var(--white);border-top:3px solid var(--blue)}
.abs{position:absolute}
.util{right:8px;top:8px;font-size:8px;color:#333}
.util span{margin:0 5px;color:#555}
.brand{left:16px;top:30px;display:flex;align-items:center;gap:8px}
.brand-dot{width:22px;height:22px;border-radius:50%;background:var(--red)}
.brand-name{font-size:14px;font-weight:600;color:#222;letter-spacing:2px;text-transform:uppercase}
.call{right:10px;top:38px;text-align:right;color:var(--blue)}
.call small{display:flex;align-items:center;justify-content:flex-end;gap:3px;font-size:9px}
.call strong{display:block;font-size:13px;font-weight:600;line-height:16px}
.nav{position:absolute;left:71px;top:82px;width:635px;height:31px;background:var(--nav);display:flex;align-items:center}
.nav a{color:#fff;text-decoration:none;font-size:10px;text-transform:uppercase;padding:0 15px;line-height:31px;border-right:1px solid #3a3a3a}
.nav a:first-child{padding-left:23px}
.search{position:absolute;right:18px;top:6px;width:136px;height:18px;background:#fff;border-radius:2px;font-size:7px;color:#bbb;padding:4px 6px}
.search svg{position:absolute;right:5px;top:3px}
.hero{position:absolute;left:83px;top:126px;width:611px;height:235px;overflow:hidden;
  background:
    radial-gradient(ellipse 120px 110px at 380px 95px,rgba(70,140,205,.9),rgba(70,140,205,0)),
    radial-gradient(ellipse 150px 160px at 330px 150px,rgba(40,95,160,.85),rgba(40,95,160,0)),
    radial-gradient(ellipse 140px 140px at 470px 150px,rgba(60,120,185,.8),rgba(60,120,185,0)),
    linear-gradient(90deg,#b7d8f2 0%,#a3ccee 40%,#7fb2e0 60%,#8cc0ea 85%,#b3d6f1 100%)}
.hero-art{position:absolute;inset:0}
.hero-copy{position:absolute;left:19px;top:48px;width:226px}
.hero h1{font-size:21px;font-weight:700;color:var(--navy);line-height:26px}
.hero h2{font-size:12.5px;font-weight:400;color:#234;margin-bottom:15px}
.hero p{font-size:8px;line-height:11.6px;color:#123}
.dots{position:absolute;left:20px;top:218px;display:flex;gap:5px}
.dots i{width:7px;height:7px;background:#fff}
.dots i:first-child{background:var(--red)}
.welcome{left:8px;top:389px;width:374px}
.welcome h3{font-size:19px;font-weight:400;color:#222;margin-bottom:12px}
.welcome h3 b{font-weight:600}
.welcome p{font-size:8.3px;line-height:11.7px;color:#666}
.welcome a{display:inline-block;margin-top:14px;font-size:8.3px;color:var(--blue);text-decoration:underline}
.services{left:429px;top:393px;width:176px}
.services h4{font-size:11.5px;font-weight:400;color:#222;text-transform:uppercase;padding-bottom:5px;border-bottom:1px solid #ccc;letter-spacing:-.3px}
.services ul{margin-top:3px}
.services li{list-style:none;font-size:8.3px;color:#666;padding:5px 4px 6px;border-bottom:2px solid #eee;margin-top:1px}
.band{position:absolute;left:0;top:536px;width:621px;height:240px;background:var(--band)}
.card{position:absolute;top:80px;width:116px;height:136px;background:#fff;border:1px solid #e0e0e0;text-align:center;padding-top:41px}
.card h5{font-size:10.4px;font-weight:600;color:#333;margin-bottom:14px}
.card p{font-size:8.4px;line-height:9.7px;color:#999;padding:0 5px}
.badge{position:absolute;top:29px;width:78px;height:78px;border-radius:50%;background:#fff;border:1px solid #e2e2e2;display:flex;align-items:center;justify-content:center}
.news{left:13px;top:792px;width:298px}
.news-head{display:flex;justify-content:space-between;align-items:flex-end;border-bottom:1px solid #ccc;padding-bottom:3px}
.news-head h3{font-size:14px;font-weight:400;color:#222}
.news-head a{font-size:7.5px;color:#333;text-decoration:none;margin-right:10px}
.item{display:flex;gap:12px;padding:14px 4px 12px;border-bottom:1px solid #ddd}
.item:last-child{border:0}
.date{width:37px;flex:none;text-align:center;margin-top:3px}
.date b{display:block;background:var(--dark);color:#fff;font-size:13px;font-weight:400;line-height:20px}
.date span{display:block;background:#e3e3e3;color:#333;font-size:11px;line-height:17px}
.item h6{font-size:11px;font-weight:400;color:#222;margin-bottom:1px}
.item p{font-size:8.3px;line-height:13px;color:#999}
.video{position:absolute;left:333px;top:810px;width:276px;height:176px;background:linear-gradient(180deg,#6f93bf 0%,#9bb6d6 35%,#2b2e33 55%,#1b1d20 80%,#8b2a22 92%,#2a3b55 100%)}
.play{position:absolute;left:120px;top:71px;width:36px;height:36px;border-radius:50%;background:#111;display:flex;align-items:center;justify-content:center}
.controls{position:absolute;left:0;bottom:0;width:100%;height:14px;background:#111}
.controls i{position:absolute;left:0;top:0;height:2px;width:30%;background:var(--red)}
.footer{position:absolute;left:0;top:1024px;width:621px;height:144px;background:var(--dark);color:#888}
.footer h4{font-size:11px;color:#fff;font-weight:400;margin-bottom:10px}
.col{position:absolute;top:24px}
.col p,.col li{font-size:7.8px;line-height:11.3px;list-style:none}
.col li{line-height:14.3px}
.cta{display:inline-block;margin-top:11px;background:var(--red);color:#fff;font-size:8px;padding:5px 8px}
.legal{position:absolute;left:0;top:1168px;width:621px;height:26px;background:#141414;color:#ccc;font-size:7.5px;text-align:center;line-height:26px}
.rule{position:absolute;left:0;top:1194px;width:621px;height:6px;background:var(--blue)}
</style>
</head>
<body>
<div class="page">
  <div class="abs util">COMPANY<span>|</span>CAREERS<span>|</span>CONTACT US</div>
  <div class="abs brand"><i class="brand-dot"></i><span class="brand-name">Vantreal Logistics</span></div>
  <div class="abs call">
    <small><svg width="8" height="8" viewBox="0 0 24 24"><path fill="#1b86c6" d="M6.6 10.8a15 15 0 0 0 6.6 6.6l2.2-2.2c.3-.3.7-.4 1-.2 1.1.4 2.3.6 3.6.6.6 0 1 .4 1 1V20c0 .6-.4 1-1 1A17 17 0 0 1 3 4c0-.6.4-1 1-1h3.5c.6 0 1 .4 1 1 0 1.3.2 2.5.6 3.6.1.3 0 .7-.2 1z"/></svg>You call, we're there</small>
    <strong>(866) 555 0142</strong>
  </div>
</div>

<nav class="nav">
  <a>Solutions</a><a>Our Process</a><a style="border:0">Industries</a>
  <div class="search">Search<svg width="11" height="11" viewBox="0 0 24 24"><circle cx="10" cy="10" r="7" fill="none" stroke="#0f4a70" stroke-width="3"/><path d="M15 15l6 6" stroke="#0f4a70" stroke-width="3"/></svg></div>
</nav>

<section class="hero">
  <div class="hero-art" role="img" aria-label="Business person touching a glowing network of supply chain technology icons"></div>
  <div class="hero-copy">
    <h1>A New Way To Think</h1>
    <h2>About Supply Chain Transformation</h2>
    <p>Vantreal Transform supply chains by managing complexity, providing data-driven insights and implementing forward-thinking innovation and actionable strategies that change business results.</p>
  </div>
  <div class="dots"><i></i><i></i><i></i><i></i></div>
</section>

<div class="page" style="background:none;border:0;pointer-events:none">
  <div class="abs welcome">
    <h3>Welcome to <b>Vantreal logistics</b></h3>
    <p>Lorem ipsum dolor sit amet, consectetuer adipiscing elit, sed diam nonummy nibh euismod tincidunt ut laoreet dolore magna aliquam erat volutpat. Ut wisi enim ad minim veniam, quis nostrud.Ullamcorper suscipit lobortis nisl ut aliquip ex ea commodo.<br>Consequat. Duis autem vel eum iriure dolor in hendrerit in vulputate velit esse molestie consequat. vel illum dolore eu feugiat nulla facilisis at vero eros et accumsan et iusto odio dignissim qui blandit.</p>
    <a>READ MORE</a>
  </div>
  <div class="abs services">
    <h4>Our Services</h4>
    <ul><li>Factory Support</li><li>Retail Distributions</li><li>After Markit Support</li><li>Critical Logistics</li></ul>
  </div>

  <div class="band">
    <div class="card" style="left:7px"><h5>Factory Support</h5><p>It is a long established fact that a reader will be distracted by the readable content of a page when looking at its</p></div>
    <div class="badge" style="left:26px"><svg width="32" height="30" viewBox="0 0 32 30"><path fill="#c8102e" d="M2 30V14l8 5v-5l8 5v-5l8 5V2h4v28z"/><rect x="7" y="22" width="3" height="3" fill="#fff"/><rect x="13" y="22" width="3" height="3" fill="#fff"/><rect x="19" y="22" width="3" height="3" fill="#fff"/></svg></div>

    <div class="card" style="left:130px"><h5>Retail Distributions</h5><p>It is a long established fact that a reader will be distracted by the readable content of a page when looking at its</p></div>
    <div class="badge" style="left:149px"><svg width="30" height="28" viewBox="0 0 30 28"><path fill="none" stroke="#c8102e" stroke-width="3" d="M1 3h5l4 15h15l3-11H8"/><circle cx="12" cy="24" r="2.5" fill="#c8102e"/><circle cx="23" cy="24" r="2.5" fill="#c8102e"/></svg></div>

    <div class="card" style="left:252px"><h5>Aftermarket Support</h5><p>It is a long established fact that a reader will be distracted by the readable content of a page when looking at its</p></div>
    <div class="badge" style="left:271px"><svg width="30" height="30" viewBox="0 0 30 30"><path stroke="#c8102e" stroke-width="4" stroke-linecap="round" d="M5 5l21 21M25 4L6 23"/><circle cx="24" cy="6" r="4" fill="#c8102e"/></svg></div>

    <div class="card" style="left:375px"><h5>Critical Logistics</h5><p>It is a long established fact that a reader will be distracted by the readable content of a page when looking at its</p></div>
    <div class="badge" style="left:394px">
      <svg width="40" height="38" viewBox="0 0 40 38">
        <defs>
          <g id="gear">
            <rect x="-2.2" y="-10" width="4.4" height="20" rx=".8"/>
            <rect x="-2.2" y="-10" width="4.4" height="20" rx=".8" transform="rotate(45)"/>
            <rect x="-2.2" y="-10" width="4.4" height="20" rx=".8" transform="rotate(90)"/>
            <rect x="-2.2" y="-10" width="4.4" height="20" rx=".8" transform="rotate(135)"/>
            <circle r="7.2"/>
          </g>
        </defs>
        <g fill="#c8102e">
          <use href="#gear" transform="translate(12 21) scale(.95)"/>
          <use href="#gear" transform="translate(28 10) scale(.75)"/>
          <use href="#gear" transform="translate(29 29) scale(.62)"/>
        </g>
        <g fill="#fff">
          <circle cx="12" cy="21" r="3"/>
          <circle cx="28" cy="10" r="2.3"/>
          <circle cx="29" cy="29" r="1.9"/>
        </g>
      </svg>
    </div>

    <div class="card" style="left:498px"><h5>Supply Chain</h5><p>It is a long established fact that a reader will be distracted by the readable content of a page when looking at its</p></div>
    <div class="badge" style="left:517px"><svg width="34" height="32" viewBox="0 0 34 32"><path fill="#c8102e" d="M2 8h10v4a3 3 0 0 0 6 0V8h4v10h-4a3 3 0 0 0 0 6h4v6H2z"/><path fill="#c8102e" d="M20 2h12v12z"/></svg></div>
  </div>

  <div class="abs news">
    <div class="news-head"><h3>Recent News</h3><a>View All</a></div>
    <div class="item"><div class="date"><b>27</b><span>Mar</span></div><div><h6>Lorem ipsum dolor sit amet</h6><p>Lorem Ipsum is simply dummy text of the printing and typesetting industry. Lorem Ipsum has been the industry's standard dummy text ever since the 1500s, when an unknown printer took a galley of type and scrambled it to make a type specimen</p></div></div>
    <div class="item"><div class="date"><b>27</b><span>Mar</span></div><div><h6>Lorem ipsum dolor sit amet</h6><p>Lorem Ipsum is simply dummy text of the printing and typesetting industry. Lorem Ipsum has been the industry's standard dummy text ever since the 1500s, when an unknown printer took a galley of type and scrambled it to make a type</p></div></div>
  </div>

  <div class="video" role="img" aria-label="Video of an offshore supply vessel at sea">
    <div class="play"><svg width="14" height="14" viewBox="0 0 14 14"><path d="M3 1l10 6-10 6z" fill="#fff"/></svg></div>
    <div class="controls"><i></i></div>
  </div>

  <footer class="footer">
    <div class="col" style="left:17px;width:225px"><h4>Become a Member!</h4><p>Lorem Ipsum is simply dummy text of the printing and typesetting industry. Lorem Ipsum has been the industry's standard dummy text ever since the 1500s, when an unknown printer took a galley of type and scrambled</p><span class="cta">Be contacted by a Vantreal Logistics</span></div>
    <div class="col" style="left:322px"><h4>POPULAR</h4><ul><li>Aftermarket Support</li><li>Critical Logistics</li><li>Retail Distributions</li><li>Factory Support</li><li>Supply Chain</li></ul></div>
    <div class="col" style="left:494px"><h4>CONTACT US</h4><p>Vantreal Logistics<br>1280 Corven Parkway<br>Ashford Point, NC 27000<br>336-555-0190<br>info@vantreal.example</p></div>
  </footer>
  <div class="legal">Copyright 2012. Vantreal Logistics, All Rights Reserved.</div>
  <div class="rule"></div>
</div>
</body>
</html>
```